Vosky - Business Card Design

Design a modern masculine business card for our business

Target Market(s)

Private Market

Industry/Entity Type

Construction

Contact Information for Business Card

Company Name - Name of Person - Address - email address - contact number

Font styles to use
Serif
Sans Serif

Colors
0094D4
00A9DD
6FCCEA
C7EBF8
E9F6FB
00AB8E
00BBA5
67D7C9
C6EFE9
E9F9F6
F0912C
F2A743
F7CA91
FBE8D2
FDF5EE

Requirements
Must have
• Use company logo provided
Nice to have
• Company Logo

```html
<!DOCTYPE html>
<html lang="en">
<head>
<meta charset="utf-8">
<title>Vosky Construction – Business Card Concept 4.A</title>
<link rel="stylesheet" href="https://fonts.googleapis.com/css2?family=Bebas+Neue&family=Michroma&family=Montserrat:wght@300;700&family=Poppins:wght@400;700&display=swap">
<style>
  :root {
    --ink: #050507;
    --paper: #ffffff;
    --accent: #ff5a24;
    --frame: #1a1a1a;
  }
  * { margin: 0; padding: 0; box-sizing: border-box; }
  html, body { width: 1200px; height: 1200px; overflow: hidden; background: var(--paper); }
  .sheet { position: relative; width: 1200px; height: 1200px; }

  .card {
    position: absolute;
    background: var(--paper);
    border: 1px solid var(--frame);
    overflow: hidden;
  }
  .card--front { left: 188px; top: 97px; width: 783px; height: 447px; }
  .card--back  { left: 201px; top: 641px; width: 770px; height: 439px; }

  .version-label {
    position: absolute; left: 43px; top: 22px;
    font-family: "Michroma", sans-serif; font-size: 27px; letter-spacing: 2px;
    color: var(--ink); font-weight: 400;
  }

  .wordmark {
    position: absolute; display: flex; align-items: center;
    font-family: "Poppins", sans-serif; font-weight: 700; color: var(--ink);
    line-height: 1;
  }
  .wordmark__square { background: var(--accent); flex: none; }
  .card--front .wordmark { left: 145px; top: 165px; gap: 22px; font-size: 108px; letter-spacing: 6px; }
  .card--front .wordmark__square { width: 44px; height: 44px; }

  .design-note {
    position: absolute; left: 62px; top: 384px;
    font-family: "Bebas Neue", sans-serif; font-size: 37px; color: var(--ink);
    letter-spacing: 0.3px; white-space: nowrap;
  }

  .stripes { position: absolute; left: 0; top: 0; width: 770px; height: 439px; }
  .stripes .band { fill: var(--ink); }
  .stripes .rule { stroke: var(--ink); stroke-width: 2.6; fill: none; }

  .card--back .wordmark { left: 59px; top: 70px; gap: 9px; font-size: 38px; letter-spacing: 2px; }
  .card--back .wordmark__square { width: 14px; height: 14px; }

  .person { position: absolute; left: 57px; top: 204px; color: var(--accent); }
  .person__name { font-family: "Montserrat", sans-serif; font-weight: 700; font-size: 37px; line-height: 1; }
  .person__role { font-family: "Montserrat", sans-serif; font-weight: 300; font-size: 26px; line-height: 1; margin-top: 6px; }

  .contact { position: absolute; left: 486px; top: 168px; list-style: none; color: var(--accent);
    font-family: "Poppins", sans-serif; font-size: 19px; line-height: 22px; }
  .contact__item { position: absolute; left: 0; display: flex; align-items: flex-start; white-space: nowrap; }
  .contact__icon { width: 22px; height: 22px; margin-right: 15px; flex: none; }
  .contact__icon * { fill: var(--accent); }
  .contact__icon .outline { fill: none; stroke: var(--accent); stroke-width: 2; }
  .contact__item--phone { top: 0; }
  .contact__item--address { top: 37px; }
  .contact__item--email { top: 95px; }
</style>
</head>
<body>
<main class="sheet">

  <section class="card card--front" aria-label="Card front concept">
    <p class="version-label">VERSION&nbsp;&nbsp;4.A</p>
    <div class="wordmark"><span class="wordmark__square"></span><span>VOSKY</span></div>
    <p class="design-note">CONSTRUCTION, INC IS MORE TALLER AND NOTICABLE HERE</p>
  </section>

  <section class="card card--back" aria-label="Card back">
    <svg class="stripes" viewBox="0 0 770 439" aria-hidden="true">
      <polygon class="band" points="404,0 461,0 500,60 443,60"/>
      <polygon class="band" points="469,0 526,0 565,60 508,60"/>
      <polygon class="band" points="534,0 591,0 630,60 573,60"/>
      <polygon class="band" points="601,0 658,0 697,60 640,60"/>
      <polygon class="band" points="666,0 723,0 762,60 705,60"/>
      <polygon class="band" points="731,0 800,0 800,60 770,60"/>

      <polygon class="band" points="0,378 41,378 2,439 0,439"/>
      <polygon class="band" points="52,378 110,378 71,439 13,439"/>
      <polygon class="band" points="119,378 178,378 139,439 80,439"/>
      <polygon class="band" points="187,378 246,378 207,439 148,439"/>
      <polygon class="band" points="256,378 314,378 275,439 217,439"/>
      <polygon class="band" points="323,378 381,378 342,439 284,439"/>

      <line class="rule" x1="510" y1="83" x2="351" y2="357"/>
    </svg>

    <div class="wordmark"><span class="wordmark__square"></span><span>VOSKY</span></div>

    <div class="person">
      <p class="person__name">NAME OF PERSON</p>
      <p class="person__role">DESIGNATION</p>
    </div>

    <ul class="contact">
      <li class="contact__item contact__item--phone">
        <svg class="contact__icon" viewBox="0 0 24 24" aria-hidden="true"><path d="M6.6 2.5l3 3.4-2 2.4c1.4 3 3.7 5.3 6.6 6.7l2.4-2 3.4 3-1.4 3.3c-.4.9-1.3 1.3-2.2 1.1C9.6 18.7 5.2 14.3 3.6 7.4c-.2-.9.2-1.8 1-2.2z"/></svg>
        <span>555 014 2288</span>
      </li>
      <li class="contact__item contact__item--address">
        <svg class="contact__icon" viewBox="0 0 24 24" aria-hidden="true"><path d="M12 2a7 7 0 0 0-7 7c0 5 7 13 7 13s7-8 7-13a7 7 0 0 0-7-7zm0 9.5A2.5 2.5 0 1 1 12 6.5a2.5 2.5 0 0 1 0 5z"/></svg>
        <span>42 Harlow Lane<br>Easton, NY 10999</span>
      </li>
      <li class="contact__item contact__item--email">
        <svg class="contact__icon" viewBox="0 0 24 24" aria-hidden="true"><rect class="outline" x="2" y="5" width="20" height="15"/><path class="outline" d="M2 5l10 9 10-9"/></svg>
        <span>hello@voskybuild.com</span>
      </li>
    </ul>
  </section>

</main>
</body>
</html>
```